Retail Seafood business needs package/label design

In need of packaging/label design for multiple seafood products such as sword fish, halibut, cod fish, scallops, mahi, catfish, and lobster tails

```html
<!DOCTYPE html>
<html lang="en">
<head>
<meta charset="utf-8">
<title>Mediterranean Tuna in Olive Oil – Label</title>
<link href="https://fonts.googleapis.com/css2?family=Barlow+Condensed:wght@300;400;600&family=Great+Vibes&family=Open+Sans:wght@400&display=swap" rel="stylesheet">
<style>
  :root {
    --page-bg: #f4f4f4;
    --label-white: #ffffff;
    --deep-teal: #064b4d;
    --sand: #e7e0cd;
    --on-teal: #ffffff;
  }
  * { box-sizing: border-box; margin: 0; padding: 0; }
  html, body {
    width: 1200px;
    height: 899px;
    overflow: hidden;
    background: var(--page-bg);
  }
  .label {
    position: absolute;
    left: 312px;
    top: 20px;
    width: 576px;
    height: 859px;
    background: var(--label-white);
    box-shadow: 0 10px 40px rgba(0,0,0,0.08);
    overflow: hidden;
  }
  .label__hero {
    position: absolute;
    left: 0; top: 0;
    width: 576px;
    height: 485px;
  }
  .hero-illustration {
    position: absolute;
    left: 174px;
    top: 0;
    width: 233px;
    height: 458px;
    background: linear-gradient(180deg, #ebe5d4 0%, var(--sand) 60%, #efe9da 100%);
    border-radius: 0 0 70px 40px / 0 0 140px 90px;
    opacity: 0.85;
  }
  .brand {
    position: absolute;
    left: 247px;
    top: 88px;
    width: 100px;
    display: flex;
    align-items: center;
    justify-content: center;
    gap: 6px;
  }
  .brand__square {
    width: 10px;
    height: 10px;
    background: var(--deep-teal);
    flex: none;
  }
  .brand__name {
    font-family: "Barlow Condensed", sans-serif;
    font-weight: 600;
    font-size: 25px;
    line-height: 0.95;
    color: var(--deep-teal);
    letter-spacing: 0.5px;
  }
  .product-title {
    position: absolute;
    left: 68px;
    top: 215px;
    width: 460px;
    font-family: "Barlow Condensed", sans-serif;
    font-weight: 600;
    font-size: 57px;
    line-height: 1;
    color: var(--deep-teal);
    letter-spacing: -0.3px;
    white-space: nowrap;
  }
  .product-subtitle {
    position: absolute;
    left: 69px;
    top: 272px;
    font-family: "Barlow Condensed", sans-serif;
    font-weight: 400;
    font-size: 35px;
    line-height: 1;
    color: var(--deep-teal);
  }
  .net-weight {
    position: absolute;
    left: 70px;
    top: 362px;
    font-family: "Barlow Condensed", sans-serif;
    font-weight: 400;
    font-size: 20px;
    line-height: 1;
    color: var(--deep-teal);
  }
  .label__band {
    position: absolute;
    left: 0;
    top: 485px;
    width: 576px;
    height: 374px;
    background: var(--deep-teal);
    color: var(--on-teal);
    text-align: center;
  }
  .quality-script {
    position: absolute;
    left: 0; right: 0;
    top: 18px;
    font-family: "Great Vibes", cursive;
    font-size: 70px;
    line-height: 1.2;
  }
  .band-copy {
    position: absolute;
    left: 76px;
    width: 424px;
    top: 134px;
    font-family: "Open Sans", sans-serif;
    font-size: 11.4px;
    line-height: 14.4px;
  }
  .natural-badge {
    position: absolute;
    left: 0; right: 0;
    top: 277px;
    font-family: "Barlow Condensed", sans-serif;
    line-height: 1;
  }
  .natural-badge__main {
    display: block;
    font-weight: 600;
    font-size: 35px;
  }
  .natural-badge__sub {
    display: block;
    font-weight: 300;
    font-size: 25px;
    margin-top: -3px;
  }
</style>
</head>
<body>
  <main class="label">
    <section class="label__hero">
      <div class="hero-illustration" role="img" aria-label="Engraved-style sand-coloured drawing of a fish head with scales, hanging downward"></div>
      <div class="brand">
        <span class="brand__square"></span>
        <span class="brand__name">MARLOW<br>COVE</span>
      </div>
      <h1 class="product-title">MEDITERRANEAN TUNA</h1>
      <p class="product-subtitle">IN OLIVE OIL</p>
      <p class="net-weight">NET WT. 15 OZ (426G)</p>
    </section>
    <section class="label__band">
      <p class="quality-script">Premiun Quality</p>
      <p class="band-copy">Lorem ipsum dolor sit amet, consectetuer adipiscing elit, sed diam nonummy nibh euismod tincidunt ut laoreet dolore magna aliquam erat Lorem ipsum dolor sit amet, consectetuer adipiscing elit, sed diam nonummy nibh euismod tincidunt ut laoreet dolore magna aliquam erat Lorem ipsum dolor sit amet, consectetuer adipiscing elit, sed diam nonummy tincidunt ut laoreet dolore magna aliquam erat</p>
      <p class="natural-badge">
        <span class="natural-badge__main">NATURAL</span>
        <span class="natural-badge__sub">PRODUCT</span>
      </p>
    </section>
  </main>
</body>
</html>
```